Electrical & Communications Company Wordpress Themed Website Design

Hi everyone,

I need a wordpress themed website designed for a new company based in Sydney Australia called "VELTRIX". It delivers electrical and communication services to the domestic and commercial sectors.

It needs to be the FULL/COMPLETE wordpress theme! A clean and easy to use site.

Please guys take the time to look at these competitors sites:

www.tapnovo.com.au
www.harbelwiring.com.au
www.qul.com.au
www.lumavoltics.com.au
www.corbinwiring.com.au
www.fendrasparkies.com.au

Please use these site for ideas only!!! we want to be original.

(If you would like to add electrical and communications to the logo that is O.K.)

Note: These logo's are registered trademarks of veltrix pty ltd.

Accreditation:

Ubta member (Federated wiring and signalling guild)

PLEASE CHECK THE WEB PLANNING LAYOUT BELOW FOR ROUGH IDEA
Updates

Have requested to increase payment to $400 and now guarantee payment!

Hi guys, forgot to mention i would like to see the business phone number prominently some where with a call to action.As we are a service business and need people to easly be able to see our contact number. Maybe top right courner but open to ideas. 

 Guys/Girls this is for a complete working word press theme that i can load up on the sever and access thru wordpress admin. Code etc

Industry/Entity Type

Communications

Requirements
Must have
• - Logo Provided must be used
• - Themes and colours to be consisted with with brand
• - Fully customizable
• - Have a social share button from shariq.com
• - Must be the full/complete theme for word press
Nice to have
• - pixtorvault
• - contactform
• - would like zenda orbit pay quidlo displayed
• - Guarantee logo or something
Should not have
• - Please don't waste your or our time submitting templates or copies of other sites original only!

```html
<!DOCTYPE html>
<html lang="en">
<head>
<meta charset="utf-8">
<title>Veltrix – Electrical &amp; Communications</title>
<link rel="stylesheet" href="https://fonts.googleapis.com/css2?family=Noto+Serif:wght@400;700&family=Arimo:wght@400;700&family=Open+Sans:wght@400&display=swap">
<style>
:root{
  --page-blue:#0a3f91;
  --page-blue-light:#1a7fd0;
  --brand-red:#d3141c;
  --brand-red-dark:#b70d15;
  --ink:#222;
  --ink-soft:#444;
  --ink-muted:#666;
  --line:#d8d8d8;
  --panel:#fff;
  --panel-head:#ececec;
}
*{box-sizing:border-box;margin:0;padding:0}
html,body{width:1200px;height:1152px;overflow:hidden}
body{
  background:radial-gradient(ellipse 700px 180px at 600px 0,var(--page-blue-light),transparent 70%),linear-gradient(var(--page-blue),#07347e);
  font-family:"Arimo",Arial,sans-serif;color:var(--ink);position:relative;
}
.site{position:absolute;left:143px;top:42px;width:894px;height:1092px;background:var(--panel);border-radius:4px 4px 0 0;overflow:hidden}
.site-header{position:absolute;left:0;top:0;width:100%;height:80px;background:linear-gradient(#fff,#f1f1f1)}
.header-swoosh{position:absolute;left:250px;top:0}
.logo{position:absolute;left:14px;top:14px;display:flex;align-items:center;gap:10px}
.logo-dot{width:46px;height:46px;border-radius:50%;background:var(--brand-red)}
.logo-name{font-family:"Noto Serif",serif;font-weight:700;font-size:38px;color:#555;letter-spacing:1px}
.call-cta{position:absolute;right:18px;top:20px;font-family:"Noto Serif",serif;font-size:30px;color:var(--brand-red)}
.main-nav{position:absolute;left:0;top:80px;width:100%;height:44px;border-top:1px solid var(--line);border-bottom:1px solid var(--line);background:#fafafa;display:flex;align-items:center;padding-left:20px}
.main-nav a{font-family:"Noto Serif",serif;font-size:13px;color:#333;text-decoration:none;padding:0 28px;border-right:1px solid var(--line);line-height:20px}
.main-nav a:last-of-type{border-right:0}
.search{position:absolute;left:640px;top:13px;display:flex;gap:10px}
.search input{width:155px;height:20px;border:1px solid #ccc;border-radius:3px;font-size:10px;padding:0 4px;color:#aaa}
.search button{height:20px;padding:0 6px;font-size:10px;font-family:"Noto Serif",serif;background:var(--brand-red);border:1px solid #900;border-radius:3px;color:#fff}
.hero{position:absolute;left:22px;top:146px;width:593px;height:255px;border-radius:4px;background:linear-gradient(90deg,#cfd3d8 0%,#e9e9e9 45%,#b9cde0 75%,#6fa4d6 100%)}
.promo{position:absolute;left:622px;width:263px;height:84px;border:1px solid #a30a12;border-radius:3px;background:linear-gradient(#f0636a,var(--brand-red) 50%,var(--brand-red-dark));color:#fff;font-family:"Noto Serif",serif;font-size:21px;display:flex;align-items:center}
.promo svg{position:absolute;left:10px}
.promo span{position:absolute;left:84px;text-shadow:0 1px 1px rgba(0,0,0,.35)}
.promo-hours{top:150px}.promo-hours span{left:124px;line-height:22px}
.promo-callout{top:237px}
.promo-pricing{top:324px}
.promo-pricing span{left:84px}
.panel{position:absolute;border:1px solid var(--line);border-radius:4px;background:var(--panel)}
.tabs{left:24px;top:439px;width:592px;height:369px}
.tab-bar{position:absolute;left:-1px;top:-1px;width:592px;height:36px;border-bottom:1px solid var(--line);display:flex;font-family:"Noto Serif",serif;font-weight:700;font-size:14px}
.tab-bar span{display:block;text-align:center;line-height:40px;height:36px}
.tab-active{width:190px;border:1px solid var(--line);border-bottom:1px solid #fff;border-radius:4px 4px 0 0;background:#fff;margin-bottom:-1px}
.tab-bar span:nth-child(2){width:180px}.tab-bar span:nth-child(3){width:190px}
.intro-title{position:absolute;left:38px;top:80px;width:540px;font-family:"Open Sans",sans-serif;font-size:18px;line-height:22px;color:#444}
.intro-text{position:absolute;left:39px;top:137px;width:510px;font-size:11px;line-height:14.5px;color:#333}
.feature-list{position:absolute;top:216px;list-style:none;font-size:12px;color:#444}
.feature-list li{height:20px;padding-left:20px;position:relative}
.feature-list li::before{content:"→";position:absolute;left:0;top:-2px;font-size:14px;color:#111}
.list-a{left:37px}.list-b{left:237px}
.btn{display:inline-block;border:1px solid #bbb;border-radius:4px;background:linear-gradient(#fff,#e3e3e3);font-family:"Noto Serif",serif;font-size:12px;color:#444;padding:2px 7px}
.tabs .btn{position:absolute;right:12px;bottom:12px}
.testimonial{left:22px;top:815px;width:594px;height:159px;overflow:hidden}
.testimonial-photo{position:absolute;right:0;top:0;width:255px;height:100%;background:linear-gradient(90deg,#fff 0%,#e6e8ea 25%,#cfd4d9 100%)}
.quote-mark{position:absolute;font-family:"Noto Serif",serif;font-size:54px;color:#ddd;line-height:1}
.testimonial h2{position:absolute;left:37px;top:6px;font-family:"Noto Serif",serif;font-weight:400;font-size:20px;color:#111}
.testimonial p{position:absolute;left:38px;top:37px;width:400px;font-size:12.5px;line-height:22px;color:#222}
.testimonial a{position:absolute;left:38px;top:136px;font-family:"Noto Serif",serif;font-size:10px;color:var(--brand-red)}
.side-box{left:623px;width:264px}
.side-head{height:38px;background:linear-gradient(#fafafa,var(--panel-head));border-bottom:1px solid var(--line);border-radius:4px 4px 0 0;font-family:"Noto Serif",serif;font-size:15px;color:#555;padding:11px 6px}
.contact{top:440px;height:238px}
.form-row{position:absolute;left:6px;font-size:12px;color:#333}
.form-field{position:absolute;left:75px;width:175px;height:18px;border:1px solid #999;background:#fff}
.contact .btns{position:absolute;left:68px;top:210px;display:flex;gap:7px}
.contact .btn{font-size:13px;padding:1px 6px}
.blog{top:688px;height:288px}
.post{position:absolute;left:7px;width:250px;font-size:11.5px;line-height:15px;color:#333}
.post b{display:block;font-size:12px;color:#333}
.post .more{display:block;text-align:right;font-weight:700;font-size:11px;color:#222;margin-top:5px;padding-right:3px}
.site-footer{position:absolute;left:0;top:987px;width:100%;height:105px;border-top:1px solid var(--line)}
.guarantee-seal{position:absolute;left:35px;top:16px;width:86px;height:86px;border-radius:50%;background:radial-gradient(#f4d23c,#c99a0f)}
.pay{position:absolute;top:26px;font-family:"Arimo",sans-serif;font-weight:700;font-size:22px;color:#1a3f8f}
.pay-quidlo{left:568px}
.pay-zenda{left:712px;top:22px;width:76px;height:46px;border:1px solid #ccc;display:flex;align-items:center;justify-content:center;font-size:18px}
.pay-orbit{left:802px;top:22px;display:flex;align-items:center;gap:5px;font-size:15px;color:var(--brand-red)}
.pay-orbit i{width:20px;height:20px;border-radius:50%;background:#f19a1a;display:block}
.copyright{position:absolute;left:0;bottom:0;width:100%;height:20px;border-top:1px solid var(--line);text-align:center;font-size:10px;letter-spacing:.5px;line-height:18px;color:#222}
</style>
</head>
<body>
<div class="site">
  <header class="site-header">
    <svg class="header-swoosh" width="160" height="80" viewBox="0 0 160 80"><path d="M10 0 C60 5 90 40 110 80 L130 80 C110 40 90 8 40 0Z" fill="#ddd"/></svg>
    <div class="logo"><span class="logo-dot"></span><span class="logo-name">VELTRIX</span></div>
    <div class="call-cta">Call Us:555.010.482</div>
  </header>
  <nav class="main-nav">
    <a href="#">Home</a><a href="#">About</a><a href="#">Service</a><a href="#">Solutions</a><a href="#">News</a><a href="#">Contacts</a>
    <form class="search"><input type="text" value="Search..."><button type="button">Search</button></form>
  </nav>

  <div class="hero" role="img" aria-label="Photo of stripped copper cables beside a smiling support operator with a headset at a computer"></div>

  <div class="promo promo-hours">
    <svg width="110" height="70" viewBox="0 0 110 70"><text x="0" y="40" font-family="Arimo,sans-serif" font-weight="700" font-size="38" fill="#111">24</text><circle cx="78" cy="34" r="24" fill="none" stroke="#fff" stroke-width="3"/><path d="M78 34 L78 18 M78 34 L90 30" stroke="#fff" stroke-width="3" stroke-linecap="round"/></svg>
    <span>24hours 7<br>days a week</span>
  </div>
  <div class="promo promo-callout">
    <svg width="60" height="70" viewBox="0 0 60 70"><path d="M10 8 C4 12 4 24 12 38 C20 52 30 62 42 64 C48 64 52 60 52 56 L42 46 C38 48 34 50 30 46 C26 40 22 34 20 28 C18 22 22 20 26 18 L20 6 C16 4 13 6 10 8Z" fill="#9a0b10"/></svg>
    <span style="left:72px">No Callout Fee</span>
  </div>
  <div class="promo promo-pricing">
    <svg width="60" height="70" viewBox="0 0 60 70"><path d="M16 32 V22 a14 14 0 0 1 28 0 V32" fill="none" stroke="#ccc" stroke-width="5"/><rect x="10" y="30" width="40" height="32" rx="8" fill="#ddd"/><circle cx="30" cy="44" r="4" fill="#a30a12"/></svg>
    <span>Fixed Pricing</span>
  </div>

  <section class="panel tabs">
    <div class="tab-bar"><span class="tab-active">Who We are?</span><span>What We Do</span><span>Our Current Projects</span></div>
    <h1 class="intro-title">Lorem Ipsum is simply dummy text of the printing and typesetting industry.</h1>
    <p class="intro-text">Lorem Ipsum is simply dummy text of the printing and typesetting industry. Lorem Ipsum has been the industry's standard dummy text ever since the 1500s, when an unknown printer took a galley of type and scrambled it to make a type specimen book. It has survived not only five centuries,</p>
    <ul class="feature-list list-a"><li>Lorem Ipsum is simply</li><li>Lorem Ipsum is simply</li><li>Lorem Ipsum is simply</li><li>Lorem Ipsum is simply</li><li>Lorem Ipsum is simply</li></ul>
    <ul class="feature-list list-b"><li>Lorem Ipsum is simply</li><li>Lorem Ipsum is simply</li><li>Lorem Ipsum is simply</li><li>Lorem Ipsum is simply</li><li>Lorem Ipsum is simply</li></ul>
    <span class="btn">Read more</span>
  </section>

  <section class="panel testimonial">
    <div class="testimonial-photo" role="img" aria-label="Portrait photo of a smiling satisfied customer"></div>
    <span class="quote-mark" style="left:2px;top:22px">“</span>
    <span class="quote-mark" style="left:410px;top:80px">”</span>
    <h2>Tesimonial</h2>
    <p>Thanks Veltrix ... What a refreshing change to find an electrical contractor who offers efficient, prompt service and has respect for the customer – with the added reassurance of a Satisfaction Guarantee!</p>
    <a href="#">Read more</a>
  </section>

  <aside class="panel side-box contact">
    <div class="side-head">Contact Us</div>
    <span class="form-row" style="top:57px">Name:</span><span class="form-field" style="top:53px"></span>
    <span class="form-row" style="top:81px">Email:</span><span class="form-field" style="top:77px"></span>
    <span class="form-row" style="top:105px">Phone:</span><span class="form-field" style="top:101px"></span>
    <span class="form-row" style="top:130px">Message:</span><span class="form-field" style="top:126px;height:68px"></span>
    <div class="btns"><span class="btn">Submit</span><span class="btn">Clear</span></div>
  </aside>

  <aside class="panel side-box blog">
    <div class="side-head">Latest Blog</div>
    <div class="post" style="top:56px"><b>08.09.2010</b>Lorem Ipsum is simply dummy text of the printing and typesetting industry.<span class="more">Read more</span></div>
    <div class="post" style="top:136px"><b>08.09.2010</b>Lorem Ipsum is simply dummy text of the printing and typesetting industry.<span class="more">Read more</span></div>
    <div class="post" style="top:214px"><b>08.09.2010</b>Lorem Ipsum is simply dummy text of the printing and typesetting industry.<span class="more">Read more</span></div>
  </aside>

  <footer class="site-footer">
    <span class="guarantee-seal"></span>
    <span class="pay pay-quidlo">QUIDLO</span>
    <span class="pay pay-zenda">ZENDA</span>
    <span class="pay pay-orbit"><i></i>ORBIT PAY</span>
    <div class="copyright">© 2007-2010 Veltrix . All Rights Reserved</div>
  </footer>
</div>
</body>
</html>
```